Dr Mira Thalen, Orthopaedic Hand Surgeon

I am an orthopaedic hand surgeon and need business cards that reflect the surgery I do. I operate on bones, ligaments, tendons, and soft tissues. I can do microsurgery (surgery under an operating microscope) - including connecting ends of cut nerves and arteries in the fingers together. As an orthopaedic surgeon, I also fix fractures and manage orthopaedic trauma in the rest of the body. I favour black as a colour, and have some pictures of hand X-rays that you can use in the design, if you think that would look good (feel free to crop).
Updates

Hi all. Thank you for all your submissions so far. Please note that I have updated my project brief. I would like to emphasise that use of the logos that I have provided is optional, and if used, I would very much prefer the logo not to dominate the card, but add to the overall aesthetic of the card. Warm regards, Mira

Target Market(s)

Referring medical practitioners, hand therapists, patients

Industry/Entity Type

Healthcare

Contact Information for Business Card

Dr Mira Thalen
Orthopaedic Hand Surgeon
MBBS BSc (Med), MIntPH (Merit), FCWES (Ortho), FUPelV

Font styles to use
Serif

Colors

Designer to choose colors to be used in the design.

Requirements
Must have
• Space for:
• 2 addresses (a PO Box Address and a consulting suite address) - to be confirmed
• 1 phone number - to be confirmed
Nice to have
• Please choose one of the FCWES logos (I included 3 - colour, black reverse, and greyscale); if you include this in the design, IT SHOULD NOT DOMINATE THE CARD, but be smaller and more discreet.
• I have also attached the FUPelV logo (colour and greyscale); if you choose to include this in the design, IT SHOULD NOT DOMINATE THE CARD, but be smaller and more discreet.
• I would love to be able to update details on the card as time goes on, and thus would like to own the template for the card as well.
• Also I would love discussion with regard to any changes on the card, if I am not completely happy with the design, and would like to discuss things such as ease of printing, finish on the cards (matte, polish) etc.
Should not have
• I don't like the card to look too crowded

```html
<!DOCTYPE html>
<html lang="en">
<head>
<meta charset="utf-8">
<title>Dr Mira Thalen – Business Card</title>
<link rel="stylesheet" href="https://fonts.googleapis.com/css2?family=Questrial&display=swap">
<style>
  :root {
    --backdrop: #e9e9e7;
    --card: #ffffff;
    --ink: #111111;
    --accent: #1db84a;
    --xray-light: #f4f4f4;
    --xray-mid: #dcdcdc;
  }
  * { box-sizing: border-box; margin: 0; padding: 0; }
  html, body {
    width: 1200px;
    height: 891px;
    overflow: hidden;
    background: var(--backdrop);
  }
  .canvas {
    position: relative;
    width: 1200px;
    height: 891px;
    font-family: "Questrial", sans-serif;
    color: var(--ink);
  }
  .card {
    position: absolute;
    left: 280px;
    width: 640px;
    height: 356px;
    background: var(--card);
    box-shadow: 0 4px 18px rgba(0,0,0,0.12);
    overflow: hidden;
  }
  .card--front { top: 48px; }
  .card--back { top: 487px; }
  .card__art {
    position: absolute;
    inset: 0;
  }
  .identity {
    position: absolute;
    left: 330px;
    right: 22px;
    top: 176px;
    text-align: right;
  }
  .identity__name {
    font-size: 42px;
    font-weight: 400;
    letter-spacing: -0.5px;
    line-height: 1;
    white-space: nowrap;
  }
  .identity__initial { color: var(--accent); }
  .identity__role {
    margin-top: 10px;
    font-size: 15px;
    letter-spacing: 0.3px;
  }
  .identity__credentials {
    margin-top: 4px;
    font-size: 9.5px;
    letter-spacing: 0.2px;
    white-space: nowrap;
  }
  .contact-slots {
    position: absolute;
    left: 78px;
    top: 96px;
    list-style: none;
    color: var(--accent);
    font-size: 22px;
    letter-spacing: -0.3px;
  }
  .contact-slots li { margin-bottom: 22px; }
</style>
</head>
<body>
<main class="canvas">

  <section class="card card--front" aria-label="Business card front">
    <svg class="card__art" width="640" height="356" viewBox="0 0 640 356">
      <defs>
        <linearGradient id="xray-front" x1="0" y1="0" x2="1" y2="1">
          <stop offset="0" stop-color="var(--xray-mid)"/>
          <stop offset="1" stop-color="var(--xray-light)"/>
        </linearGradient>
      </defs>
      <rect x="70" y="0" width="230" height="150" fill="url(#xray-front)"
            role="img" aria-label="Line drawing of a hand skeleton reaching down from the top edge"/>
      <polyline points="218,0 326,164 179,356" fill="none" stroke="var(--accent)" stroke-width="4"/>
    </svg>
    <div class="identity">
      <h1 class="identity__name">Dr <span class="identity__initial">M</span>ira Thalen</h1>
      <p class="identity__role">orthopaedic hand surgeon</p>
      <p class="identity__credentials">MBBS BSc (Med), MIntPH (Merit), FCWES (Ortho), FUPelV</p>
    </div>
  </section>

  <section class="card card--back" aria-label="Business card back">
    <svg class="card__art" width="640" height="356" viewBox="0 0 640 356">
      <defs>
        <linearGradient id="xray-back" x1="1" y1="0" x2="0" y2="1">
          <stop offset="0" stop-color="var(--xray-mid)"/>
          <stop offset="1" stop-color="var(--xray-light)"/>
        </linearGradient>
      </defs>
      <rect x="420" y="20" width="220" height="170" fill="url(#xray-back)"
            role="img" aria-label="Line drawing of a hand skeleton reaching in from the right edge"/>
      <line x1="392" y1="58" x2="380" y2="300" stroke="var(--accent)" stroke-width="2"/>
    </svg>
    <ul class="contact-slots">
      <li>- 2 addresses</li>
      <li>- 1 phone number</li>
    </ul>
  </section>

</main>
</body>
</html>
```